Clean A3 Menu Brochure for a Pizza Shop

We are looking for a cleaner design to replace our old menu (please find attached) and we already have a draft (please find attached). The menu should be A3 and easy to read with a very subtle marble background and clean font for the menu items. It can be folded for leafleting or be used flat on the store counter. It should not be overcrowded, and the prices for each item should be easy to understand. Ideally we would like images for each section in the menu body, for example chicken for the Chicken Sides (feel free to leave space or add any photos - these will be replaced with our own photos in a later revision) and these should feel natural to the menu (please see Inspo pictures). The deals will be split into 2 sections: The main 3 deals which will come with photos once we do a photoshoot and a more compact list of all the other deals. We have left the front page quite empty as we’re not sure what will go on it, except for 1 large image like in the old menu, our store details and that we can be found on QuickDine, RoamBites and Platevan.

Industry/Entity Type

Fast-food

Colors

Designer to choose colors to be used in the design.

Requirements
Must have
• Bold, eye-catching fonts for the deals without losing readability. The customers should clearly see what items come with each deal. The background and menu should be kept clean with pops of colour from images around the menu.

```html
<!DOCTYPE html>
<html lang="en">
<head>
<meta charset="utf-8">
<title>Crimson Crust Pizza – Menu</title>
<link href="https://fonts.googleapis.com/css2?family=Montserrat:wght@500;600;700;800&family=Questrial&display=swap" rel="stylesheet">
<style>
  :root {
    --brand-red: #c0182c;
    --ink: #111111;
    --ink-soft: #333333;
    --paper: #ffffff;
    --blush: #fbf1f3;
    --stage: #e9e9ea;
    --photo-warm: #c98a55;
    --photo-cool: #d9dadc;
    --photo-mint: #9fd0c8;
  }
  * { box-sizing: border-box; margin: 0; padding: 0; }
  html, body { width: 1200px; height: 1200px; overflow: hidden; }
  body { background: var(--stage); position: relative; font-family: "Questrial", "Helvetica Neue", sans-serif; color: var(--ink); }

  .menu-sheet {
    position: absolute; left: 30px; top: 197px; width: 1140px; height: 806px;
    background: var(--paper); overflow: hidden;
    box-shadow: 0 2px 6px rgba(0,0,0,.18);
  }
  .sheet-art { position: absolute; inset: 0; width: 100%; height: 100%; }
  .block { position: absolute; }

  .brand-name { left: 34px; top: 40px; font-family: "Montserrat", sans-serif; font-weight: 800; font-size: 29px; letter-spacing: 0; color: var(--brand-red); white-space: nowrap; }
  .brand-phone { left: 34px; top: 102px; font-family: "Montserrat", sans-serif; font-weight: 600; font-size: 26px; letter-spacing: .5px; }
  .brand-address { left: 34px; top: 148px; font-size: 13px; line-height: 18px; letter-spacing: .6px; color: var(--ink-soft); text-transform: uppercase; font-style: normal; }
  .brand-rule { left: 34px; top: 202px; width: 304px; height: 1.5px; background: var(--brand-red); }

  .section-title { font-family: "Montserrat", sans-serif; font-weight: 800; font-size: 21px; letter-spacing: .3px; }
  .toppings-title { left: 34px; top: 228px; }

  .margherita { left: 34px; top: 266px; font-family: "Montserrat", sans-serif; font-weight: 700; font-size: 10px; }
  .price-grid { display: grid; grid-template-columns: repeat(5, 32px); font-size: 8px; line-height: 10px; text-align: center; color: var(--ink-soft); }
  .price-grid.standard { left: 28px; top: 286px; }
  .price-grid.premium { left: 282px; top: 638px; }

  .pizza-list { left: 34px; top: 338px; width: 380px; list-style: none; font-family: "Montserrat", sans-serif; font-weight: 600; font-size: 9.4px; line-height: 11.9px; }

  .extra-toppings { left: 40px; top: 683px; width: 470px; font-size: 9.6px; line-height: 12.5px; color: var(--ink-soft); }

  .sides-title { left: 500px; top: 40px; }
  .side-list { left: 500px; top: 78px; width: 300px; list-style: none; font-size: 9.6px; line-height: 11.8px; color: var(--ink-soft); }

  .chicken-title { left: 500px; top: 356px; }
  .chicken-list { left: 500px; top: 408px; width: 382px; list-style: none; font-size: 15px; line-height: 19.4px; color: var(--ink-soft); }
  .chicken-list li { display: flex; justify-content: space-between; white-space: nowrap; gap: 12px; }
  .chicken-list .cost { width: 100px; flex: none; }
</style>
</head>
<body>
  <main class="menu-sheet">
    <svg class="sheet-art" viewBox="0 0 1140 806" preserveAspectRatio="none" aria-hidden="true">
      <defs>
        <linearGradient id="foodTones" x1="0" y1="0" x2="1" y2="1">
          <stop offset="0" stop-color="#d9dadc"/>
          <stop offset=".45" stop-color="#c98a55"/>
          <stop offset=".8" stop-color="#b8743d"/>
          <stop offset="1" stop-color="#9fd0c8"/>
        </linearGradient>
      </defs>
      <path class="blush-band" d="M560 0 H760 C740 120 790 220 850 290 C900 350 900 420 880 500 C860 580 840 640 800 690 L720 806 H430 C520 720 600 640 640 540 C680 420 580 320 540 200 C520 130 535 60 560 0 Z" fill="var(--blush)"/>
      <path class="red-wave" d="M290 806 C460 770 600 720 720 700 C780 690 820 680 840 672 L900 806 Z" fill="var(--brand-red)"/>
    </svg>
    <svg class="sheet-art" viewBox="0 0 1140 806" preserveAspectRatio="none" role="img" aria-label="Food photography: overhead marble table with pasta, a tomato, dips, a vegetable pizza and roasted cauliflower">
      <path d="M745 0 H1140 V806 H760 C780 760 800 700 830 665 C900 620 915 560 905 500 C895 420 925 360 885 300 C825 240 760 200 745 120 Z" fill="url(#foodTones)"/>
    </svg>

    <h1 class="block brand-name">CRIMSON CRUST PIZZA</h1>
    <p class="block brand-phone">0207 946 0321</p>
    <address class="block brand-address">crimsoncrustpizza.co.uk<br>12 Fennel Lane, Ashvale AV3 7QP</address>
    <div class="block brand-rule"></div>

    <h2 class="block section-title toppings-title">PICK YOUR TOPPINGS</h2>
    <p class="block margherita">Margherita – Cheese &amp; Tomato</p>
    <div class="block price-grid standard">
      <span>7"</span><span>10"</span><span>13"</span><span>15"</span><span>18"</span>
      <span>£5.99</span><span>£7.99</span><span>£9.99</span><span>£11.99</span><span>£15.99</span>
    </div>

    <ul class="block pizza-list">
      <li>Make Your Own - Any 4 toppings of your choice</li>
      <li>Pepperoni Passion - Double Pepperoni, Double Cheese</li>
      <li>Hawaiian – Ham, Mushrooms, Pineapple</li>
      <li>House Special - ?</li>
      <li>Coriander Chilli Chicken – Garlic Butter, Chicken Tikka, Red Onions, Chillies, Fresh Coriander</li>
      <li>Vegetarian – Red Onions, Mushrooms, Mixed Peppers, Sweetcorn, Fresh Tomatoes</li>
      <li>Veggie Volcano – Garlic Butter Base, Red Onions, Black Olives, Fresh Tomatoes, Chillies</li>
      <li>Mexican Spice – Spicy Beef, Mexican Chicken, Red Onions, Mixed Peppers, Jalapeños, Fresh Tomatoes</li>
      <li>Meat Feast – Pepperoni, Ham, Spicy Pork, Spicy Beef</li>
      <li>Alligator – Salami, Pepperoni, Ham, Smoky Sausage, Bacon</li>
      <li>Greek Style – Pepperoni, Red Onions, Black Olives, Fresh Tomatoes, Feta Cheese, Mixed Herbs</li>
      <li>Oriental Express - Chinese Chicken, Mushrooms, Mixed Peppers, Sweetcorn, Pineapple</li>
      <li>BBQ Feast – BBQ Sauce, Pepperoni, Meatballs, Red Onions</li>
      <li>BBQ Chicken Sizzler - BBQ Sauce, Bacon, Chicken, Red Onions</li>
      <li>Caribbean Tuna – Red Onions, Mixed Peppers, Jalapeños, Fresh Tomatoes, Tuna</li>
      <li>Space For Another Pizza - lorem ipsum</li>
      <li>Space For Another Pizza - lorem ipsum</li>
      <li>Space For Another Pizza - lorem ipsum</li>
      <li>Space For Another Pizza - lorem ipsum</li>
    </ul>
    <div class="block price-grid premium">
      <span>7"</span><span>10"</span><span>13"</span><span>15"</span><span>18"</span>
      <span>£6.99</span><span>£10.99</span><span>£12.99</span><span>£14.99</span><span>£16.99</span>
    </div>

    <p class="block extra-toppings">Extra Toppings – Garlic Butter, Pizza Sauce, BBQ Sauce, Cheese, Salami, Pepperoni, Ham, Smoky Sausage, Kebab, Meatballs, Bacon, Spicy Pork, Chicken, Spicy Beef, Chinese Chicken, Chicken Tikka, Tandoori Chicken, Red Onions, Mushrooms, Mixed Peppers, Pineapple, Sweetcorn, Jalapeños, Black Olives, Fresh Tomatoes, Feta Cheese, Chillies, Fresh Garlic, Mixed Herbs, Fresh Coriander, Tuna, Prawns, Anchovies</p>

    <h2 class="block section-title sides-title">SIDE ORDERS</h2>
    <ul class="block side-list">
      <li>Garlic Bread – 4 slices £2.49 | £4.49</li>
      <li>+ Add cheese for 50p</li>
      <li>Garlic Pizza Bread – freshly baked 10" pizza £7.99</li>
      <li>+ Add cheese for 50p</li>
      <li>+ Upgrade to a 13" for £2 extra</li>
      <li>Fries £2.99 | £4.99</li>
      <li>Curly Fries £4.99 | £8.99</li>
      <li>+ Add cheese for 50p</li>
      <li>Wedges - comes with 2 dips £4.99 | £8.99</li>
      <li>Potato Skins with Cheese £4.99 | £8.99</li>
      <li>+ Add a topping for 50p</li>
      <li>Mixed Salad £3.99</li>
      <li>+ Add chicken for 99p</li>
      <li>Greek Salad £4.99</li>
      <li>Coleslaw £1.99</li>
      <li>Mozzarella Sticks – 8 pieces £4.99 | £8.99</li>
      <li>Onion Rings – 8 pieces £3.49 | £5.99</li>
      <li>Cream Cheese Jalapeños – 8 pieces £4.99 | £8.99</li>
      <li>BBQ Ribs £5.99 | £9.99</li>
    </ul>

    <h2 class="block section-title chicken-title">CHICKEN SIDES</h2>
    <ul class="block chicken-list">
      <li><span>Chicken Strips – 8 pieces</span><span class="cost">£4.99 | £8.99</span></li>
      <li><span>+ Double up for</span><span class="cost">£4.00 extra</span></li>
      <li><span>BBQ Wings – 8 pieces</span><span class="cost">£4.99 | £8.99</span></li>
      <li><span>+ Double up for</span><span class="cost">£4.00 extra</span></li>
      <li><span>Spicy Chicken Dippers – 8 pieces</span><span class="cost">£4.99 | £8.99</span></li>
      <li><span>+ Double up for</span><span class="cost">£4.00 extra</span></li>
      <li><span>Hot Wings – 8 pieces</span><span class="cost">£4.99 | £8.99</span></li>
      <li><span>+ Double up for</span><span class="cost">£4.00 extra</span></li>
      <li><span>Chicken Nuggets - 8 pieces</span><span class="cost">£4.99 | £8.99</span></li>
    </ul>
  </main>
</body>
</html>
```